Restaurant service company needs a website!

I am looking for a skilled web designer/developer to create a professional, responsive, and easy-to-navigate website for my company, which specializes in servicing restaurant cooking equipment. The site should communicate trust, reliability, and technical expertise to our target audience, restaurant owners, managers, and commercial kitchen operators. I have included the company logos, if any other format for them is needed please let me know.

Target Market(s)

restaurant owners, managers, and commercial kitchen operators

Industry/Entity Type

Commercial Kitchen Equipment Service

Coding

Coded - Design and coding required

Number of Pages Required

1 page

Font styles to use
Serif
Sans Serif

Requirements
Must have
• Contact and service request forms, Click-to-call functionality for mobile, Clean, modern layout with strong visuals, Easy navigation, mobile-friendly
Nice to have
• Testimonials or Reviews, If possible a click-to-text functionality for mobile.
Should not have
• Any mention of Refrigeration or HVAC, "Free Quotes"

```html
<!DOCTYPE html>
<html lang="en">
<head>
<meta charset="utf-8">
<title>Ironvale Kitchen Service</title>
<link rel="stylesheet" href="https://fonts.googleapis.com/css2?family=Plus+Jakarta+Sans:wght@400;500;600;700;800&family=Outfit:wght@400;500&display=swap">
<style>
:root{
  --teal:#0a6580;
  --teal-dark:#07546b;
  --ink:#1c1c1c;
  --deep-green:#0f2c14;
  --muted:#6b6b6b;
  --pale:#d8e6ea;
  --card:#f4f4f4;
  --white:#ffffff;
  --star:#e6cf12;
  --red:#e84a4a;
}
*{box-sizing:border-box;margin:0;padding:0}
html,body{width:1200px;height:3125px;overflow:hidden}
body{position:relative;background:var(--white);font-family:"Plus Jakarta Sans",Arial,sans-serif;color:var(--ink)}
.abs{position:absolute}
.brand{font-weight:700;color:var(--teal);font-size:20px;letter-spacing:.5px;display:flex;align-items:center;gap:8px}
.brand .mark{width:14px;height:14px;background:var(--teal)}
.nav-links{left:474px;top:30px;display:flex;gap:36px;font-size:12px;font-weight:500}
.hours{left:994px;top:30px;font-size:12px;font-weight:600;display:flex;align-items:center;gap:8px}
.hours i{width:7px;height:7px;border-radius:50%;background:var(--red)}
.hero-band{left:0;top:74px;width:1200px;height:509px;background:var(--teal)}
.hero-notch{left:0;top:580px}
.hero-photo{top:74px;height:499px}
.hero-tags{left:268px;width:664px;top:176px;text-align:center;color:#e4eef1;font-size:13px;font-weight:500}
.hero-tags span{margin:0 10px}
.hero-title{left:268px;width:664px;top:206px;text-align:center;color:var(--white);font-size:42px;font-weight:700;line-height:50px;letter-spacing:-.5px}
.checks{display:flex;gap:26px;font-size:13px}
.checks span{display:flex;align-items:center;gap:6px}
.hero-checks{left:268px;width:664px;top:320px;justify-content:center;color:#e8f1f3}
.btn-dark{left:527px;top:368px;width:147px;height:40px;border-radius:20px;background:#062d24;color:var(--white);font-size:15px;font-weight:600;display:flex;align-items:center;justify-content:space-between;padding:0 5px 0 16px}
.btn-dark b{width:30px;height:30px;border-radius:50%;background:var(--white);display:flex;align-items:center;justify-content:center}
.hero-feats{left:318px;top:462px;display:flex;color:var(--white);font-size:12px;font-weight:500;line-height:15px}
.feat{display:flex;align-items:center;gap:10px;padding:0 20px;border-right:1px solid rgba(255,255,255,.25)}
.feat:last-child{border:none}
.feat .ic{width:30px;height:30px;border-radius:50%;background:rgba(0,0,0,.18);display:flex;align-items:center;justify-content:center}
.experts h2{font-size:35px;font-weight:600;line-height:42px;letter-spacing:-.5px}
.experts p{margin-top:16px;font-size:11.5px;color:var(--muted);line-height:18px;width:370px}
.ticks{margin-top:34px;display:grid;grid-template-columns:187px 190px;row-gap:22px;font-size:12.5px;font-weight:600;color:var(--teal)}
.ticks span{display:flex;align-items:center;gap:8px}
.avail{margin-top:38px;width:281px;height:50px;border-radius:12px;background:var(--teal);color:var(--white);font-size:11.5px;line-height:17px;padding:8px 20px}
.form-card{left:690px;top:651px;width:348px;height:422px;border-radius:10px;background:var(--pale);padding:0 24px}
.form-card h3{font-size:12.5px;font-weight:600;margin:34px 0 26px}
.field{height:48px;background:var(--white);border-radius:3px;margin-bottom:16px;font-size:9px;color:#777;display:flex;align-items:center;justify-content:space-between;padding:0 18px}
.btn-schedule{height:64px;border-radius:3px;background:var(--teal);color:var(--white);font-size:13px;font-weight:500;display:flex;align-items:center;justify-content:center;margin-top:22px}
.scale-photo{left:995px;top:940px;width:112px;height:150px;border-radius:40px 40px 10px 10px;background:radial-gradient(circle at 50% 60%,#f2f2f2 0 30%,#9aa0a4 55%,#2a2a2a 90%)}
.center-head{left:0;width:1200px;text-align:center}
.sec-title{font-size:35px;font-weight:600;letter-spacing:-.5px}
.sec-sub{font-size:11.5px;color:var(--muted);line-height:18px}
.svc{top:1257px;width:190px}
.svc .ic{width:40px;height:40px;border-radius:8px;background:var(--teal);display:flex;align-items:center;justify-content:center}
.svc h4{margin-top:14px;font-size:15px;font-weight:600}
.svc p{margin-top:10px;font-size:11px;line-height:17px;color:var(--muted)}
.more{left:395px;top:1426px;width:411px;height:110px;border-radius:12px;background:var(--teal);color:var(--white);padding:26px 20px}
.more h4{font-size:15px;font-weight:600}
.more p{font-size:11px;line-height:18px;margin-top:4px;width:185px}
.more .call{position:absolute;right:20px;top:35px;width:173px;height:40px;border-radius:20px;background:var(--white);color:var(--teal);font-weight:600;font-size:15px;display:flex;align-items:center;justify-content:center}
.rapid{left:38px;top:1586px;width:1125px;height:374px;border-radius:14px;background:var(--teal);color:var(--white)}
.rapid h2{position:absolute;left:113px;top:40px;font-size:33px;font-weight:600;line-height:40px}
.rapid .lead{position:absolute;left:629px;top:41px;width:380px;font-size:15px;line-height:18px}
.rapid hr{position:absolute;left:113px;top:136px;width:860px;border:none;border-top:1px solid rgba(255,255,255,.15)}
.benefit{position:absolute;width:400px;display:flex;gap:22px}
.benefit .ic{width:58px;flex:none;display:flex;justify-content:center}
.benefit h4{font-size:15.5px;font-weight:600}
.benefit p{font-size:11px;line-height:17.5px;margin-top:8px;color:#e3eef1}
.eyebrow{left:70px;top:2024px;display:flex;align-items:center;gap:14px;font-family:"Outfit",sans-serif;font-size:19px;color:var(--teal)}
.eyebrow i{width:18px;height:18px;border-radius:50%;background:#2a84e0;box-shadow:0 0 0 4px #bcdaf5}
.testi-title{left:70px;top:2052px;font-family:"Outfit",sans-serif;font-size:55px;font-weight:400;color:var(--deep-green);letter-spacing:-.5px}
.testi-lead{left:692px;top:2052px;width:450px;font-family:"Outfit",sans-serif;font-size:22px;line-height:22px;color:#5a5a5a}
.review{top:2162px;width:342px;height:218px;border-radius:14px;background:var(--card);box-shadow:0 6px 14px rgba(0,0,0,.06);padding:30px 30px}
.review .who{display:flex;gap:16px;align-items:flex-start}
.review .av{width:44px;height:44px;border-radius:50%;background:#dcdcdc}
.review .name{font-family:"Outfit",sans-serif;font-size:17px;margin-top:2px}
.review .role{font-size:11px;color:#8a8a8a;margin-top:10px}
.review p{font-size:9.5px;line-height:17.5px;color:#8a8a8a;margin-top:16px}
.stars{margin-top:12px;color:var(--star);font-size:24px;letter-spacing:2px}
.cta-title{left:112px;top:2530px;font-size:42px;font-weight:700;line-height:47px;letter-spacing:-.5px}
.cta-checks{left:112px;top:2694px;color:var(--teal);font-size:12.5px}
.btn-teal{left:112px;top:2735px;width:146px;height:40px;border-radius:20px;background:var(--teal);color:var(--white);font-size:15px;font-weight:600;display:flex;align-items:center;justify-content:center}
.appliances{left:620px;top:2405px;width:550px;height:405px;border-radius:40px;background:radial-gradient(ellipse at 50% 55%,#f4f4f4 0 45%,#e7e2dc 70%,#fff 100%)}
.footer{left:0;top:2840px;width:1200px;height:285px;background:var(--teal);color:var(--white)}
.footer .logo{position:absolute;left:150px;top:46px;height:44px;padding:0 14px;background:var(--white);display:flex;align-items:center}
.footer .about{position:absolute;left:150px;top:112px;width:270px;font-size:11.5px;line-height:18px}
.socials{position:absolute;left:150px;top:166px;display:flex;gap:18px}
.socials i{width:12px;height:12px;border-radius:50%;background:var(--white)}
.fcol{position:absolute;top:48px;font-size:12.5px}
.fcol h5{font-size:15px;font-weight:600;margin-bottom:18px}
.fcol div{margin-bottom:13px}
.footer .rule{position:absolute;left:0;top:225px;width:1200px;border-top:1px solid rgba(255,255,255,.18)}
.footer .copy{position:absolute;left:0;width:1200px;top:256px;text-align:center;font-size:11.5px}
</style>
</head>
<body>

<header>
  <div class="abs brand" style="left:105px;top:22px"><span class="mark"></span>IRONVALE</div>
  <nav class="abs nav-links"><span>About Us</span><span>Services</span><span>Our Blog</span><span>Contact</span></nav>
  <div class="abs hours"><i></i>24 Hour Services</div>
</header>

<section class="hero">
  <div class="abs hero-band"></div>
  <svg class="abs hero-notch" width="1200" height="32" viewBox="0 0 1200 32"><path d="M262 0 L295 30 L900 30 L934 0 Z" fill="#0a6580"/></svg>
  <div class="abs hero-photo" role="img" aria-label="Cast iron skillet on a stovetop" style="left:10px;width:258px;background:linear-gradient(160deg,#6a6c72,#2d2f36 45%,#1e2a66)"></div>
  <div class="abs hero-photo" role="img" aria-label="Stainless steel gas range knobs in a commercial kitchen" style="left:932px;width:256px;background:linear-gradient(200deg,#c8a16e,#6d625a 40%,#2d3238)"></div>
  <div class="abs hero-tags"><span>Maintenances</span>•<span>Repairs</span>•<span>Improvements</span></div>
  <h1 class="abs hero-title">Need to improve or repair your equipment? We can help!</h1>
  <div class="abs checks hero-checks">
    <span><svg width="11" height="9"><path d="M1 4.5 4 7.5 10 1" stroke="#fff" fill="none" stroke-width="1.5"/></svg>Fast Estimates</span>
    <span><svg width="11" height="9"><path d="M1 4.5 4 7.5 10 1" stroke="#fff" fill="none" stroke-width="1.5"/></svg>100% Commitment-Free</span>
  </div>
  <div class="abs btn-dark">Call Us Now<b><svg width="14" height="14" viewBox="0 0 24 24"><path d="M6.6 10.8a15 15 0 0 0 6.6 6.6l2.2-2.2a1 1 0 0 1 1-.25 11 11 0 0 0 3.6.6 1 1 0 0 1 1 1V20a1 1 0 0 1-1 1A17 17 0 0 1 3 4a1 1 0 0 1 1-1h3.5a1 1 0 0 1 1 1c0 1.25.2 2.45.57 3.57a1 1 0 0 1-.25 1z" fill="#062d24"/></svg></b></div>
  <div class="abs hero-feats">
    <div class="feat"><span class="ic"><svg width="14" height="14"><circle cx="7" cy="7" r="5.5" stroke="#fff" fill="none"/><path d="M4.5 7 6.3 8.8 9.5 5.5" stroke="#fff" fill="none"/></svg></span>Satisfaction<br>Guarantee</div>
    <div class="feat"><span class="ic"><svg width="14" height="14"><circle cx="7" cy="7" r="5.5" stroke="#fff" fill="none"/><path d="M7 4v3.3l2 1.2" stroke="#fff" fill="none"/></svg></span>24H<br>Availability</div>
    <div class="feat"><span class="ic"><svg width="14" height="14"><path d="M7 13s4.5-4.5 4.5-7.5a4.5 4.5 0 0 0-9 0C2.5 8.5 7 13 7 13z" stroke="#fff" fill="none"/><circle cx="7" cy="5.5" r="1.6" stroke="#fff" fill="none"/></svg></span>Local<br>Professional</div>
    <div class="feat"><span class="ic"><svg width="14" height="14"><rect x="2" y="3" width="10" height="9" rx="1.5" stroke="#fff" fill="none"/><path d="M2 6h10M5 1.5v3M9 1.5v3" stroke="#fff"/></svg></span>Flexible<br>Appointments</div>
  </div>
</section>

<section class="abs experts" style="left:150px;top:684px">
  <h2>Your Kitchen<br>Equipment Experts</h2>
  <p>We specialize in restaurant equipment services across the US. Our comprehensive solutions ensure your kitchen operates at its best.</p>
  <div class="ticks">
    <span>✓ Repair and Installation</span><span>✓ Inspections</span>
    <span>✓ Maintenance</span><span>✓ Cost-Effective</span>
    <span>✓ Equipment Servicing</span><span>✓ Energy-efficient solutions</span>
  </div>
  <div class="avail">We're available 24/7 for fast service. Contact us at (555) 014-2290</div>
</section>

<form class="abs form-card">
  <h3>Pick The Services You Want</h3>
  <div class="field">Full Name</div>
  <div class="field">Email address</div>
  <div class="field">Phone</div>
  <div class="field">Services type<svg width="12" height="7"><path d="M1 1l5 5 5-5" stroke="#333" fill="none"/></svg></div>
  <div class="btn-schedule">Get Schedule</div>
</form>
<div class="abs scale-photo" role="img" aria-label="Kitchen weighing scale"></div>

<section>
  <h2 class="abs center-head sec-title" style="top:1125px">Our Services</h2>
  <p class="abs center-head sec-sub" style="top:1183px;left:425px;width:350px">From ovens to fryers, we've got your essential kitchen equipment covered!</p>
  <div class="abs svc" style="left:170px"><div class="ic"><svg width="20" height="20" viewBox="0 0 20 20"><path d="M4 16 12 8M11 3l6 6-3 3-6-6z" stroke="#fff" stroke-width="2" fill="none"/></svg></div><h4>Oven repair</h4><p>Gas and electric oven repair, calibration, and maintenance</p></div>
  <div class="abs svc" style="left:395px"><div class="ic"><svg width="22" height="18" viewBox="0 0 22 18"><path d="M2 15 8 4h12l-4 11z" fill="#fff"/></svg></div><h4>Fryer maintenance</h4><p>Deep fryer repair, cleaning, and oil filtration system service</p></div>
  <div class="abs svc" style="left:620px"><div class="ic"><svg width="20" height="18"><rect x="3" y="2" width="6" height="5" fill="#fff"/><rect x="3" y="9" width="14" height="3" fill="#fff"/><rect x="3" y="14" width="14" height="2" fill="#fff"/></svg></div><h4>Cooking Utensil</h4><p>Mixers, processors, and specialty cooking tools repair</p></div>
  <div class="abs svc" style="left:845px"><div class="ic"><svg width="20" height="20" viewBox="0 0 20 20"><path d="M4 4l12 12M16 4 4 16" stroke="#fff" stroke-width="2.4"/></svg></div><h4>Dishwasher repair</h4><p>Commercial dishwasher, conveyor, and sanitization system service</p></div>
  <div class="abs more"><h4>More service?</h4><p>Let us know how we can help keep your kitchen running smoothly!</p><div class="call">Call Us Now</div></div>
</section>

<section class="abs rapid">
  <h2>Rapid, Reliable, and<br>Guaranteed Service</h2>
  <p class="lead">We're dedicated to keeping your restaurant equipment in top shape, ensuring minimal downtime and maximum efficiency.</p>
  <hr>
  <div class="benefit" style="left:113px;top:156px"><div class="ic"><svg width="48" height="52" viewBox="0 0 48 52"><circle cx="24" cy="20" r="14" stroke="#fff" stroke-width="3" fill="none"/><path d="M17 20l5 5 9-9M14 32 8 46l7-2 3 6 6-13M34 32l6 14-7-2-3 6-6-13" stroke="#fff" stroke-width="3" fill="none"/></svg></div><div><h4>Satisfaction Guarantee</h4><p>Rest assured, our certified technicians deliver top-quality service and lasting solutions.</p></div></div>
  <div class="benefit" style="left:620px;top:156px"><div class="ic"><svg width="48" height="48" viewBox="0 0 48 48"><path d="M8 4h20l8 8v30H8z" stroke="#fff" stroke-width="3" fill="none"/><path d="M14 20h16M14 28h10M14 36h8M26 38l16-16 4 4-16 16h-4z" stroke="#fff" stroke-width="3" fill="none"/></svg></div><div><h4>Fast Estimates</h4><p>Get no-obligation estimates tailored to your specific equipment needs. Experience transparent pricing and reliable service.</p></div></div>
  <div class="benefit" style="left:113px;top:273px"><div class="ic"><svg width="52" height="52" viewBox="0 0 52 52"><circle cx="26" cy="26" r="22" stroke="#fff" stroke-width="3" fill="none"/><circle cx="26" cy="26" r="13" stroke="#fff" stroke-width="3" fill="none"/><text x="26" y="30" font-size="11" font-weight="700" fill="#fff" text-anchor="middle" font-family="Plus Jakarta Sans,sans-serif">24h</text></svg></div><div><h4>24/7 Emergency Service</h4><p>Unexpected equipment failure? Our expert technicians are ready to provide immediate assistance, day or night.</p></div></div>
  <div class="benefit" style="left:620px;top:273px"><div class="ic"><svg width="56" height="50" viewBox="0 0 56 50"><path d="M4 20c0-10 9-16 20-16s20 6 20 16-9 16-20 16c-3 0-5 0-8-1L6 40l4-9c-4-3-6-7-6-11z" stroke="#fff" stroke-width="3" fill="none"/><path d="M16 18h16M16 25h10" stroke="#fff" stroke-width="3"/><path d="M46 22c4 3 6 7 6 11 0 4-2 7-5 9l3 7-9-4" stroke="#fff" stroke-width="3" fill="none"/></svg></div><div><h4>100% Commitment-Free</h4><p>Discuss your equipment concerns with us. We offer expert advice with no strings attached.</p></div></div>
</section>

<section>
  <div class="abs eyebrow"><i></i>Partner in Kitchen Services</div>
  <h2 class="abs testi-title">Costumer Testimonials</h2>
  <p class="abs testi-lead">Delivering expert kitchen solutions ensure your operation from repairs to installations our team provides durable high-quality</p>
  <article class="abs review" style="left:70px"><div class="who"><span class="av"></span><div><div class="name">Daniel Ross</div><div class="role">Homeowner</div></div></div><p>Ironvale has helped me keep a reliable and efficient kitchen. I used to struggle with finding proper repair but the team always delivers great service</p><div class="stars">★★★★★</div></article>
  <article class="abs review" style="left:447px"><div class="who"><span class="av"></span><div><div class="name">Maria Lenz</div><div class="role">Property Manager</div></div></div><p>Ironvale has helped me keep a reliable and efficient kitchen. I used to struggle with finding proper repair but the team always delivers great service</p><div class="stars">★★★★★</div></article>
  <article class="abs review" style="left:823px"><div class="who"><span class="av"></span><div><div class="name">Peter Hale</div><div class="role">Homeowner</div></div></div><p>Ironvale has helped me keep a reliable and efficient kitchen. I used to struggle with finding proper repair but the team always delivers great service</p><div class="stars">★★★★★</div></article>
</section>

<section>
  <h2 class="abs cta-title">Ready to optimize your<br>kitchen's performance?<br>Let’s Talk!</h2>
  <div class="abs checks cta-checks"><span>✓ Fast Estimates</span><span>✓ 100% Commitment-Free</span></div>
  <div class="abs btn-teal">Call Us Now</div>
  <div class="abs appliances" role="img" aria-label="White kitchen appliances: coffee maker, kettle, blender, toaster, mixer and food processor"></div>
</section>

<footer class="abs footer">
  <div class="logo"><span class="brand">IRONVALE</span></div>
  <p class="about">Ironvale is the leading provider for restaurant cooking equipment service and repair.</p>
  <div class="socials"><i></i><i></i><i></i><i></i><i></i></div>
  <div class="fcol" style="left:865px"><h5>Company</h5><div>About us</div><div>Services</div><div>Our Blog</div><div>Contact</div></div>
  <div class="fcol" style="left:1000px"><h5>Legal</h5><div>Terms</div><div>Privacy</div><div>Cookies</div><div>License</div></div>
  <div class="rule"></div>
  <div class="copy">©2023 Ironvale. All rights reserved</div>
</footer>

</body>
</html>
```